Admin Backend Redesign

We need a redesign for our backend which supoosed to make the backoffice look more modern!

I will add screenshots of the backoffice so you know what data will be shown in the Admin.

Have in mind that the users of this backend are Doctors. We need a clinical look, modern and sharp. The backoffice is responsive, have that in mind. We need the backoffice to look as professional as possible.

The theme used for the website is: http://velmora.quillstack-sample.com/

ON the main page of the backoffice, under every widget i need some space to write an explanation what the widget is about.

The color code used in our logo and website is #57aad4 combined with white.

We are open for ideas!
Updates

Project Deadline Extended
Reason: Designs are ok, but nothing innovative. Please use more modern designs!

Project Deadline Extended
Reason: Havent recieved a perfect design yet. Please read instructions carefully! Thank you

Project Deadline Extended
Reason: Hey everybody, sorry for the delay. We will decide in 3 days. If anyone wants to add a Design, that would be great.

Target Market(s)

Doctors, therapists

Industry/Entity Type

It Professional

Font styles to use
Sans Serif

Requirements
Must have
• Must look uptodate, modern, like new back offices look nowadays

```html
<!DOCTYPE html>
<html lang="de">
<head>
<meta charset="utf-8">
<title>Velmora Backoffice – Dashboard</title>
<link href="https://fonts.googleapis.com/css2?family=Open+Sans:wght@400;600;700&display=swap" rel="stylesheet">
<style>
  :root{
    --brand:#57aad4;
    --brand-dark:#3f93bf;
    --brand-light:#7cc0e2;
    --page:#eceef0;
    --card:#ffffff;
    --line:#e3e6e9;
    --text:#4a4f55;
    --muted:#8a9096;
    --footer:#3a3d41;
  }
  *{box-sizing:border-box;margin:0;padding:0}
  html,body{width:672px;height:1200px;overflow:hidden}
  body{font-family:"Open Sans",Arial,sans-serif;color:var(--text);background:var(--page);position:relative;font-size:7px}

  .topbar{position:absolute;left:0;top:0;width:672px;height:58px;background:#fff;border-bottom:1px solid var(--line)}
  .brand{position:absolute;left:14px;top:14px;display:flex;align-items:center;gap:6px}
  .brand-mark{width:26px;height:26px;background:#4a4f55}
  .brand-name{font-size:13px;font-weight:700;color:#4a4f55}
  .user{position:absolute;right:12px;top:17px;display:flex;align-items:center;gap:6px;font-size:8px;color:var(--text)}
  .user-avatar{width:22px;height:22px;background:linear-gradient(#9aa3ab,#6e767d)}
  .user-toggle{width:12px;height:12px;background:var(--brand)}

  .sidebar{position:absolute;left:0;top:58px;width:139px;height:1092px;background:var(--brand)}
  .sidebar-head{height:22px;background:var(--brand-dark);display:flex;justify-content:flex-end;align-items:center;padding-right:10px}
  .sidebar-head span{width:9px;height:9px;border:1.5px solid #fff}
  .menu{list-style:none;margin-top:4px}
  .menu li{height:24px;display:flex;align-items:center;padding-left:10px;gap:6px;color:#fff;font-size:7.5px}
  .menu li.active{background:var(--brand-light)}
  .menu li i{width:6px;height:6px;background:#fff;opacity:.85}

  .crumb{position:absolute;left:139px;top:58px;width:533px;height:28px;background:#fff;display:flex;align-items:center;padding-left:18px;gap:5px;font-size:7.5px;border-bottom:1px solid var(--line)}

  .card{position:absolute;width:240px;background:var(--card);box-shadow:0 1px 2px rgba(0,0,0,.08)}
  .col-l{left:158px}.col-r{left:420px}
  .card-head{height:32px;background:var(--brand);color:#fff;font-size:10px;display:flex;align-items:center;padding:0 10px;gap:12px}
  .search{flex:0 0 110px;height:13px;background:var(--brand-dark);color:#d8eef9;font-size:6px;padding-left:5px;display:flex;align-items:center}

  .profile{height:64px;background:var(--brand);color:#fff;display:flex;align-items:center;padding:0 12px}
  .profile-icon{width:40px;height:40px;border-radius:50%;background:#fff;display:flex;align-items:center;justify-content:center}
  .profile-name{margin-left:10px;font-size:8px;display:flex;align-items:center;gap:4px}
  .profile-name b{width:9px;height:9px;border:1.5px solid #fff;border-radius:50%}
  .profile-title{margin-left:auto;text-align:right}
  .profile-title strong{display:block;font-size:17px;font-weight:400}
  .profile-title small{font-size:7px}

  .welcome{padding:10px}
  .welcome-lead{color:var(--brand);font-size:8.5px;line-height:1.35}
  .btn{display:inline-block;margin:8px 0;background:var(--brand);color:#fff;font-size:6.5px;padding:4px 10px}
  .welcome p{font-size:6.5px;line-height:1.45}

  .chart-body{padding:10px;height:146px}
  .pie-body{height:154px;position:relative}

  table{width:100%;border-collapse:collapse;font-size:6.3px}
  th{text-align:left;font-weight:600;padding:6px 8px;border-bottom:1px solid var(--line)}
  td{padding:6px 8px;border-bottom:1px solid var(--line)}
  .stars{color:#4a4f55;letter-spacing:1px}
  .table-foot{display:flex;justify-content:space-between;align-items:center;padding:7px 8px;font-size:6px;color:var(--muted)}
  .pager span{display:inline-block;border:1px solid var(--line);padding:2px 6px;color:var(--text);margin-left:2px}

  .footer{position:absolute;left:0;top:1150px;width:672px;height:50px;background:var(--footer);color:#c9ccd0;font-size:6.5px;display:flex;align-items:center;padding:0 12px}
</style>
</head>
<body>
  <header class="topbar">
    <div class="brand"><span class="brand-mark"></span><span class="brand-name">Velmora</span></div>
    <div class="user"><span class="user-avatar" role="img" aria-label="Profilfoto des Arztes"></span>Dr Conrad Halvers<span class="user-toggle"></span></div>
  </header>

  <nav class="sidebar">
    <div class="sidebar-head"><span></span></div>
    <ul class="menu">
      <li class="active"><i></i>Dashboard</li>
      <li><i></i>Mein Konto</li>
      <li><i></i>Patientenbewertungen</li>
    </ul>
  </nav>

  <div class="crumb">
    <svg width="8" height="8" viewBox="0 0 10 10"><path d="M5 1 1 5h1.5v4h2.2V6.5h.6V9h2.2V5H9z" fill="#4a4f55"/></svg>Start
  </div>

  <section class="card col-l profile" style="top:108px">
    <div class="profile-icon"><svg width="18" height="18" viewBox="0 0 20 20"><circle cx="10" cy="6" r="4" fill="#57aad4"/><path d="M2 19c0-5 3.5-7 8-7s8 2 8 7z" fill="#57aad4"/></svg></div>
    <div class="profile-name">Walter <b></b></div>
    <div class="profile-title"><strong>Profil</strong><small>Profil bearbeiten</small></div>
  </section>
  <section class="card col-r profile" style="top:108px">
    <div class="profile-icon"><svg width="22" height="18" viewBox="0 0 24 20"><circle cx="12" cy="6" r="3.6" fill="#57aad4"/><circle cx="5" cy="7" r="2.6" fill="#57aad4"/><circle cx="19" cy="7" r="2.6" fill="#57aad4"/><path d="M5 19c0-5 3-7 7-7s7 2 7 7z" fill="#57aad4"/><path d="M0 18c0-4 2-5.5 5-5.5 1 0 2 .2 2.6.6C5.5 15 5 16.5 5 18z M24 18c0-4-2-5.5-5-5.5-1 0-2 .2-2.6.6 2.1 1.9 2.6 3.4 2.6 4.9z" fill="#57aad4"/></svg></div>
    <div class="profile-name">Jennifer <b></b></div>
    <div class="profile-title"><strong>Patienten</strong><small>Patienten Verwalten</small></div>
  </section>

  <section class="card col-l" style="top:200px">
    <div class="card-head">Willkommen : Dr Mustermann</div>
    <div class="welcome">
      <div class="welcome-lead">Neque porro quisquam est qui dolorem ipsum quia dolor sit amet, consectetur, adipisci velit...</div>
      <span class="btn">Mehr Erf</span>
      <p>Lorem Ipsum is simply dummy text of the printing and typesetting industry. Lorem Ipsum has been the industry's standard dummy text ever since the 1500s, when an unknown printer took a galley of type and scrambled it to make a type specimen book.</p>
    </div>
  </section>
  <section class="card col-r" style="top:200px">
    <div class="card-head">Xxxi Tnen Fur</div>
    <div class="chart-body">
      <svg width="220" height="126" viewBox="0 0 220 126">
        <g stroke="#e6e8ea" stroke-width="1">
          <line x1="20" y1="10" x2="215" y2="10"/><line x1="20" y1="38" x2="215" y2="38"/><line x1="20" y1="66" x2="215" y2="66"/><line x1="20" y1="94" x2="215" y2="94"/><line x1="20" y1="118" x2="215" y2="118"/>
          <line x1="60" y1="10" x2="60" y2="118"/><line x1="100" y1="10" x2="100" y2="118"/><line x1="140" y1="10" x2="140" y2="118"/><line x1="180" y1="10" x2="180" y2="118"/>
        </g>
        <g fill="#8a9096" font-size="5">
          <text x="4" y="12">1.2</text><text x="4" y="40">0.9</text><text x="4" y="68">0.6</text><text x="4" y="96">0.3</text><text x="4" y="120">0</text>
        </g>
        <polyline fill="none" stroke="#f5a742" stroke-width="1.2" points="20,112 40,111 55,108 62,104 66,30 70,62 76,55 82,64 90,58 100,66 110,60 120,64 130,58 140,62 150,57 160,61 170,59 180,63 190,60 200,62 215,60"/>
      </svg>
    </div>
  </section>

  <section class="card col-l" style="top:400px">
    <div class="card-head">Pie 1</div>
    <div class="pie-body">
      <svg width="240" height="154" viewBox="0 0 240 154">
        <g transform="rotate(-90 120 77)">
          <circle cx="120" cy="77" r="29" fill="none" stroke="#f5a742" stroke-width="58" pathLength="100" stroke-dasharray="40 100"/>
          <circle cx="120" cy="77" r="29" fill="none" stroke="#5fc4d9" stroke-width="58" pathLength="100" stroke-dasharray="18 100" stroke-dashoffset="-40"/>
          <circle cx="120" cy="77" r="29" fill="none" stroke="#ea5a3a" stroke-width="58" pathLength="100" stroke-dasharray="42 100" stroke-dashoffset="-58"/>
        </g>
        <rect x="222" y="14" width="6" height="6" fill="#f5a742"/><rect x="222" y="22" width="6" height="6" fill="#5fc4d9"/><rect x="222" y="30" width="6" height="6" fill="#ea5a3a"/>
      </svg>
    </div>
  </section>
  <section class="card col-r" style="top:400px">
    <div class="card-head">Pie 2</div>
    <div class="pie-body">
      <svg width="240" height="154" viewBox="0 0 240 154">
        <g transform="rotate(-90 120 77)">
          <circle cx="120" cy="77" r="29" fill="none" stroke="#f06c1f" stroke-width="58" pathLength="100" stroke-dasharray="100 100" stroke-dashoffset="-52"/>
          <circle cx="120" cy="77" r="29" fill="none" stroke="#ffd13f" stroke-width="58" pathLength="100" stroke-dasharray="8 100"/>
          <circle cx="120" cy="77" r="29" fill="none" stroke="#9ccc3c" stroke-width="58" pathLength="100" stroke-dasharray="10 100" stroke-dashoffset="-8"/>
          <circle cx="120" cy="77" r="29" fill="none" stroke="#1a8fc7" stroke-width="58" pathLength="100" stroke-dasharray="14 100" stroke-dashoffset="-18"/>
          <circle cx="120" cy="77" r="29" fill="none" stroke="#8e44ad" stroke-width="58" pathLength="100" stroke-dasharray="6 100" stroke-dashoffset="-32"/>
          <circle cx="120" cy="77" r="29" fill="none" stroke="#e0358b" stroke-width="58" pathLength="100" stroke-dasharray="4 100" stroke-dashoffset="-38"/>
        </g>
        <rect x="222" y="14" width="6" height="6" fill="#f06c1f"/><rect x="222" y="22" width="6" height="6" fill="#ffd13f"/><rect x="222" y="30" width="6" height="6" fill="#9ccc3c"/><rect x="222" y="38" width="6" height="6" fill="#1a8fc7"/><rect x="222" y="46" width="6" height="6" fill="#e0358b"/>
      </svg>
    </div>
  </section>

  <section class="card col-l" style="top:608px">
    <div class="card-head">Stat 1 <span class="search">Search</span></div>
    <table>
      <tr><th>Name</th><th>Position</th><th>Start Date</th><th>Salary</th></tr>
      <tr><td>Gerda</td><td>Chefin</td><td>1.11.2013</td><td>$3,120</td></tr>
      <tr><td>Gerda</td><td>Chefin</td><td>1.11.2013</td><td>$3,120</td></tr>
      <tr><td>Gerda</td><td>Chefin</td><td>1.11.2013</td><td>$3,120</td></tr>
      <tr><td>Gerda</td><td>Chefin</td><td>1.11.2013</td><td>$3,120</td></tr>
      <tr><td>Gerda</td><td>Chefin</td><td>1.11.2013</td><td>$3,120</td></tr>
    </table>
    <div class="table-foot">Showing 1 to 5 of 9 entries<span class="pager"><span>Prev</span><span>Next</span></span></div>
  </section>
  <section class="card col-r" style="top:608px">
    <div class="card-head">Stat 2 <span class="search">Search</span></div>
    <table>
      <tr><th>Domain</th><th>Stimmen</th><th>Keywords</th><th>SE Keywords</th></tr>
      <tr><td>Domain.de</td><td>25 %</td><td>Gemeinsame</td><td>5K Keywords</td></tr>
      <tr><td>Domain.de</td><td>25 %</td><td>Gemeinsame</td><td>5K Keywords</td></tr>
      <tr><td>Domain.de</td><td>25 %</td><td>Gemeinsame</td><td>5K Keywords</td></tr>
      <tr><td>Domain.de</td><td>25 %</td><td>Gemeinsame</td><td>5K Keywords</td></tr>
      <tr><td>Domain.de</td><td>25 %</td><td>Gemeinsame</td><td>5K Keywords</td></tr>
    </table>
    <div class="table-foot">Showing 1 to 5 of 9 entries<span class="pager"><span>Prev</span><span>Next</span></span></div>
  </section>

  <section class="card col-l" style="top:850px">
    <div class="card-head">Stat 1 <span class="search">Search</span></div>
    <table>
      <tr><th>Name</th><th>Profilseiten</th><th>Bewertung</th></tr>
      <tr><td>Gerda</td><td>nyc ungefiel</td><td class="stars">★★★★★</td></tr>
      <tr><td>Gerda</td><td>nyc ungefiel</td><td class="stars">★★★★★</td></tr>
      <tr><td>Gerda</td><td>nyc ungefiel</td><td class="stars">★★★★★</td></tr>
      <tr><td>Gerda</td><td>nyc ungefiel</td><td class="stars">★★★★★</td></tr>
      <tr><td>Gerda</td><td>nyc ungefiel</td><td class="stars">★★★★★</td></tr>
    </table>
    <div class="table-foot">Showing 1 to 5 of 9 entries<span class="pager"><span>Prev</span><span>Next</span></span></div>
  </section>

  <footer class="footer"><span>© 2014 Company Name. All Rights Reserved.</span></footer>
</body>
</html>
```